Business Card Design Project

We need a business card for our IT services provider business. We provide services to small and medium business, and would like something that reflects the color scheme / branding on our recently updated website - www.larkbyte.com.au

The card type we have chosen is a matte laminated double sided configuration at 86mm x 54mm on 350 GSM cardboard.
Updates

Target Market(s)

Small and Medium Business owners

Industry/Entity Type

Business

Requirements
Must have
• *Details on all cards*

Company Name: LarkByte IT Pty Ltd
ABN: 62 385 219 604
Address: 47-49 Marrow Street, Kelbrook Vale, Victoria 3150
Phone: 1300 LARK BY
Fax: 03 9417 6209
Website: www.larkbyte.com.au
Logo/Handprint Icon

*Person Specific*

```html
<!DOCTYPE html>
<html lang="en">
<head>
<meta charset="utf-8">
<title>LarkByte IT – Business Card</title>
<link href="https://fonts.googleapis.com/css2?family=Arimo:wght@400;700&display=swap" rel="stylesheet">
<style>
  :root {
    --stage: #d9d9d9;
    --blue: #1d5b97;
    --blue-deep: #154a80;
    --blue-light: #2a6aa8;
    --white: #ffffff;
    --ink: #1b2533;
    --link: #2f6fb0;
  }
  * { box-sizing: border-box; margin: 0; padding: 0; }
  html, body {
    width: 1200px;
    height: 900px;
    overflow: hidden;
    background: var(--stage);
    font-family: "Arimo", Arial, sans-serif;
  }
  .sheet {
    width: 1200px;
    height: 900px;
    display: flex;
    flex-direction: column;
    align-items: center;
    justify-content: center;
    gap: 40px;
  }
  .card {
    width: 620px;
    height: 389px;
    position: relative;
    overflow: hidden;
    box-shadow: 0 8px 24px rgba(0, 0, 0, 0.18);
  }

  /* Front */
  .card--front {
    background: linear-gradient(180deg, var(--blue-light), var(--blue-deep));
  }
  .contact-person {
    position: absolute;
    left: 215px;
    top: 36px;
    color: var(--white);
    font-size: 15px;
    line-height: 1.3;
  }
  .contact-person .person-name { font-size: 18px; }
  .brand-band {
    position: absolute;
    left: 0;
    right: 0;
    top: 118px;
    height: 126px;
    background: var(--white);
  }
  .brand-band .brand-name {
    position: absolute;
    left: 180px;
    top: 26px;
    font-size: 40px;
    font-weight: 400;
    color: var(--ink);
    letter-spacing: 0.5px;
  }
  .brand-band .website {
    position: absolute;
    left: 200px;
    top: 84px;
    font-size: 15px;
    color: var(--link);
  }
  .company-details {
    position: absolute;
    left: 0;
    right: 0;
    top: 262px;
    text-align: center;
    color: var(--white);
    font-size: 13.5px;
    line-height: 1.4;
  }

  /* Back */
  .card--back {
    background: radial-gradient(ellipse at 50% 45%, var(--blue-light), var(--blue-deep) 80%);
    display: flex;
    align-items: center;
    justify-content: center;
  }
  .card--back .brand-name {
    font-size: 44px;
    font-weight: 400;
    color: var(--white);
    letter-spacing: 0.5px;
  }
</style>
</head>
<body>
  <main class="sheet">
    <section class="card card--front" aria-label="Business card front">
      <div class="contact-person">
        <p class="person-name">Tamsin Vorley</p>
        <p>555 014 027</p>
        <p>tamsin@larkbyte.com.au</p>
      </div>
      <div class="brand-band">
        <p class="brand-name">LarkByte IT</p>
        <p class="website">www.larkbyte.com.au</p>
      </div>
      <div class="company-details">
        <p>LarkByte IT Pty Ltd</p>
        <p>ABN: 62 385 219 604</p>
        <p>47-49 Marrow Street, Kelbrook Vale, Victoria 3921</p>
        <p>Phone: 1300 LARK BY</p>
        <p>Fax: 03 9417 6209</p>
      </div>
    </section>

    <section class="card card--back" aria-label="Business card back">
      <p class="brand-name">LarkByte IT</p>
    </section>
  </main>
</body>
</html>
```